VERIDAX Need a luxury modern business card designed.

Need a luxury modern business card designed. refer to the uploaded files for the company name and logo in the zip file under source files. i will making my descion on monday. so please send in before then so if we need to edit we will have the time. we have a trade show coming up and im on a deadline for printer.

Target Market(s)

high end clients

Contact Information for Business Card

Company nAme and logo. Calvin Ostrow Co-Founder / Project Manager Office # 416-555-0193 Cell # 416-555-0147 VERIDAX.CA Calvin@veridax.ca

Font styles to use
Other font styles liked:
• Modern

Requirements
Must have
• Company name and logo, contact info, using the black, gold and white color scheme.

```html
<!DOCTYPE html>
<html lang="en">
<head>
<meta charset="utf-8">
<title>VERIDAX Business Card</title>
<link href="https://fonts.googleapis.com/css2?family=Work+Sans:wght@300;400;600;700&display=swap" rel="stylesheet">
<style>
  :root {
    --page-bg: #dcdcdc;
    --card-charcoal: #323335;
    --emboss-dark: #262729;
    --gold: #a99b63;
    --white: #ffffff;
  }
  * { box-sizing: border-box; margin: 0; padding: 0; }
  html, body {
    width: 1200px;
    height: 1125px;
    overflow: hidden;
    background: var(--page-bg);
    font-family: "Work Sans", Arial, sans-serif;
  }
  .sheet {
    width: 1200px;
    height: 1125px;
    display: flex;
    flex-direction: column;
    align-items: center;
    justify-content: center;
    gap: 40px;
  }
  .card {
    width: 875px;
    height: 500px;
    background: var(--card-charcoal);
    box-shadow: 0 6px 18px rgba(0,0,0,0.25);
    position: relative;
  }

  /* Back side: tone-on-tone company name */
  .card-back {
    display: flex;
    align-items: center;
    justify-content: center;
  }
  .back-lockup { text-align: center; color: var(--emboss-dark); }
  .back-lockup .company-name {
    font-size: 64px;
    font-weight: 300;
    letter-spacing: 12px;
    line-height: 1;
  }
  .back-lockup .tagline {
    margin-top: 14px;
    font-size: 15px;
    font-weight: 400;
    letter-spacing: 7px;
  }

  /* Front side */
  .card-front {
    display: flex;
    align-items: center;
  }
  .brand-block {
    width: 440px;
    display: flex;
    flex-direction: column;
    align-items: center;
  }
  .brand-block .company-name {
    color: var(--white);
    font-size: 60px;
    font-weight: 300;
    letter-spacing: 10px;
    line-height: 1;
  }
  .brand-block .tagline {
    margin-top: 14px;
    color: var(--white);
    font-size: 14px;
    font-weight: 400;
    letter-spacing: 6px;
  }
  .divider {
    width: 2px;
    height: 250px;
    background: var(--gold);
  }
  .contact-block {
    padding-left: 30px;
  }
  .person-name {
    color: var(--gold);
    font-size: 28px;
    font-weight: 700;
    letter-spacing: 2px;
    text-transform: uppercase;
  }
  .person-title {
    margin-top: 4px;
    color: var(--white);
    font-size: 21px;
    font-weight: 400;
    letter-spacing: 1px;
  }
  .contact-list {
    list-style: none;
    margin-top: 24px;
  }
  .contact-list li {
    display: flex;
    align-items: center;
    gap: 12px;
    color: var(--white);
    font-size: 21px;
    letter-spacing: 0.5px;
    line-height: 1.45;
  }
  .contact-icon {
    width: 18px;
    height: 18px;
    flex: none;
    fill: var(--gold);
  }
</style>
</head>
<body>
<main class="sheet">
  <section class="card card-back" aria-label="Card back">
    <div class="back-lockup">
      <div class="company-name">VERIDAX</div>
      <div class="tagline">LUXURY LANDSCAPES</div>
    </div>
  </section>

  <section class="card card-front" aria-label="Card front">
    <div class="brand-block">
      <div class="company-name">VERIDAX</div>
      <div class="tagline">LUXURY LANDSCAPES</div>
    </div>
    <div class="divider"></div>
    <div class="contact-block">
      <div class="person-name">Calvin Ostrow</div>
      <div class="person-title">Co-Founder / Project Manager</div>
      <ul class="contact-list">
        <li>
          <svg class="contact-icon" viewBox="0 0 24 24" aria-hidden="true"><path d="M6.6 10.8c1.4 2.8 3.8 5.1 6.6 6.6l2.2-2.2c.3-.3.7-.4 1-.2 1.1.4 2.3.6 3.6.6.6 0 1 .4 1 1V20c0 .6-.4 1-1 1C10.6 21 3 13.4 3 4c0-.6.4-1 1-1h3.5c.6 0 1 .4 1 1 0 1.3.2 2.5.6 3.6.1.3 0 .7-.2 1z"/></svg>
          <span>416-555-0193</span>
        </li>
        <li>
          <svg class="contact-icon" viewBox="0 0 24 24" aria-hidden="true"><path d="M7 1h10c1.1 0 2 .9 2 2v18c0 1.1-.9 2-2 2H7c-1.1 0-2-.9-2-2V3c0-1.1.9-2 2-2zm0 3v14h10V4H7zm5 15.5a1 1 0 1 0 0 2 1 1 0 0 0 0-2z"/></svg>
          <span>416-555-0147</span>
        </li>
        <li>
          <svg class="contact-icon" viewBox="0 0 24 24" aria-hidden="true"><path d="M2 5h20v14H2V5zm2 2v.5l8 5 8-5V7H4zm0 2.8V17h16V9.8l-8 5-8-5z"/></svg>
          <span>Calvin@veridax.ca</span>
        </li>
        <li>
          <svg class="contact-icon" viewBox="0 0 24 24" aria-hidden="true"><path d="M12 2a10 10 0 1 0 0 20 10 10 0 0 0 0-20zm6.9 6h-2.9a15 15 0 0 0-1.4-3.6A8 8 0 0 1 18.9 8zM12 4c.8 1.2 1.5 2.5 1.9 4h-3.8c.4-1.5 1.1-2.8 1.9-4zM4.3 14a8 8 0 0 1 0-4h3.4a16 16 0 0 0 0 4H4.3zm.8 2h2.9c.3 1.3.8 2.5 1.4 3.6A8 8 0 0 1 5.1 16zM8 8H5.1a8 8 0 0 1 4.3-3.6C8.8 5.5 8.3 6.7 8 8zm4 12c-.8-1.2-1.5-2.5-1.9-4h3.8c-.4 1.5-1.1 2.8-1.9 4zm2.3-6H9.7a14 14 0 0 1 0-4h4.6a14 14 0 0 1 0 4zm.3 5.6c.6-1.1 1.1-2.3 1.4-3.6h2.9a8 8 0 0 1-4.3 3.6zm1.7-5.6a16 16 0 0 0 0-4h3.4a8 8 0 0 1 0 4h-3.4z"/></svg>
          <span>VERIDAX.CA</span>
        </li>
      </ul>
    </div>
  </section>
</main>
</body>
</html>
```